Ridgeline Outfitters Business Cards

Recently had a logo done with Artfolio and now looking for a business card to go along with it.

Target Market(s)

Ridgeline Outfitters is a weapons dealer. My market will be primarily men, hunting, shooting type.

Industry/Entity Type

Business

Contact Information for Business Card

I selected double sided, but this is not required, single or double is going to be fine. I picture the logo on one side, or perhaps just the circle which contains "RO" with the remaining info on the other side.

Font styles to use
Sans Serif

Requirements
Must have
• My name: Milo Brandt
• Title: Owner
• tel: 612-555-0187
• web: www.ridgelineoutfittersmn.example
Nice to have
• I like the concept of a black business card. I would like to keep the colors monotone, black, grey, white or red. Red is acceptable because it is in the logo. I have also seen cards that are matte black with shiny black as well, perhaps for the logo (or circle RO) part of the logo.
• I will upload a couple of the logos for use, and also an example I just found of the black on black. and some others that have a nice contrast.
Should not have
• lots of colors are not wanted.

```html
<!DOCTYPE html>
<html lang="en">
<head>
<meta charset="UTF-8">
<title>Ridgeline Outfitters – Business Card</title>
<link href="https://fonts.googleapis.com/css2?family=Roboto:wght@300;400;700&display=swap" rel="stylesheet">
<style>
  :root {
    --backdrop: #1c1c1c;
    --card: #2b2b2b;
    --ink-black: #121212;
    --ink-grey: #1a1a1a;
    --accent-red: #e8262c;
    --edge-gold: #c9a21c;
  }
  * { margin: 0; padding: 0; box-sizing: border-box; }
  html, body {
    width: 1200px;
    height: 900px;
    overflow: hidden;
    background: var(--backdrop);
    font-family: "Roboto", Arial, sans-serif;
  }
  .canvas {
    position: relative;
    width: 1200px;
    height: 900px;
  }
  .card {
    position: absolute;
    width: 525px;
    height: 300px;
    background: var(--card);
    border-bottom: 4px solid var(--edge-gold);
    border-right: 2px solid var(--edge-gold);
  }
  .card--front { left: 110px; top: 140px; }
  .card--back { left: 565px; top: 460px; }

  .brand-name {
    position: absolute;
    left: 38px;
    top: 44px;
    font-weight: 700;
    font-size: 38px;
    letter-spacing: 1px;
    text-transform: uppercase;
    color: var(--ink-black);
    line-height: 1.05;
  }
  .contact {
    position: absolute;
    left: 38px;
    bottom: 34px;
    font-weight: 300;
    font-size: 14px;
    letter-spacing: 0.5px;
    color: var(--ink-grey);
    line-height: 1.6;
  }
  .contact .name { text-transform: uppercase; }
  .contact .accent { color: var(--accent-red); }

  .monogram {
    position: absolute;
    left: 50%;
    top: 50%;
    transform: translate(-50%, -50%);
    font-weight: 700;
    font-size: 110px;
    color: var(--accent-red);
    letter-spacing: 2px;
  }
</style>
</head>
<body>
  <main class="canvas">
    <section class="card card--front" aria-label="Business card front">
      <h1 class="brand-name">Ridgeline<br>Outfitters</h1>
      <div class="contact">
        <p class="name">Milo Brandt / <span class="accent">OWNER</span></p>
        <p><span class="accent">P</span> : 612 555 0187 / <span class="accent">W</span> : www.ridgelineoutfittersmn.example</p>
      </div>
    </section>

    <section class="card card--back" aria-label="Business card back">
      <p class="monogram">RO</p>
    </section>
  </main>
</body>
</html>
```